CREATE A KILLER WEBSITE DESIGN

We are a firearms training company that trains CIVILIANS (no police or military pictures - thank you!) to defend themselves and are looking for a killer design that's clean, easy to navigate and modern! We want the newest trends applied to this sight like a scrollable site so you can scroll down and see all the features. We are okay with tweaking the HTML but need the artistic design to look good. I'll provide a link to our current site along with a sight we really like so you can get an idea!

I'm supplying a PowerPoint Design we are going with from another designer so you can match the style to the new site.

PAGES: (Please use information from our current site. We like the information but just want a more polished look similar to the NWDLA site below but in our colors.)
Home - Long Form Scrolling Site. Top fold will be a video with a play button.
Falcon Institute - Seven Level Training Program Info Page That Will Contain A Video.
Contact Us - This will be a page that DOES NOT CONTAIN AN EMAIL ADDRESS. Just a contact us form
Meet The Trainer: Morgan Pellbrook

Our site:
https://www.brisklanewardens.biz

Sights We Like:
https://www.nwdefenseleague.example.com
https://quorvel.example.com
https://brantforgeworks.example.com
https://www.pelnrigear.example.com

Target Market(s)

Men and women ages 21 to 100 years old

Industry/Entity Type

Self Defense

Number of Pages Required

5+ page

Font styles to use
Sans Serif

Colors
f26267

Requirements
Must have
• Clean and engaging. Use of colors that match our logo.
Should not have
• Poor design quality

```html
<!DOCTYPE html>
<html lang="en">
<head>
<meta charset="utf-8">
<title>Brisklane Wardens</title>
<link href="https://fonts.googleapis.com/css2?family=Audiowide&family=Montserrat:ital,wght@0,400;0,500;0,600;0,700;1,400&display=swap" rel="stylesheet">
<style>
:root{
  --red:#e21f26;
  --dark:#3a3a3a;
  --darker:#2e2e2e;
  --light:#efefef;
  --text:#444;
  --muted:#777;
  --white:#fff;
  --gold:#e9a21a;
  --gray-num:#6d6d6d;
}
*{box-sizing:border-box;margin:0;padding:0}
html,body{width:1200px;height:4531px;overflow:hidden}
body{font-family:"Montserrat",sans-serif;color:var(--text);background:var(--white);position:relative}
.display{font-family:"Audiowide",sans-serif}
section,header,footer{position:absolute;left:0;width:1200px}
.abs{position:absolute}

/* header */
.site-header{top:0;height:130px;background:var(--dark);color:var(--white)}
.utility-links{top:7px;left:96px;display:flex;gap:18px;font-size:11px;font-weight:600}
.utility-links span::before{content:"";display:inline-block;width:9px;height:8px;border:1.5px solid #ccc;border-radius:2px;margin-right:5px;vertical-align:-1px}
.brand{top:52px;left:88px;width:100px;text-align:center;font-size:12px;font-weight:700;line-height:1.2}
.brand i{display:block;width:26px;height:26px;border-radius:50%;border:2px solid var(--white);margin:0 auto 5px}
.tagline{top:52px;left:213px;color:var(--red);font-size:15px;letter-spacing:2px}
.main-nav{top:93px;left:214px;display:flex;gap:20px;font-size:17px;font-weight:500}
.login{top:46px;left:826px;font-size:12px;font-weight:600}
.urgent{top:40px;left:906px;width:203px;height:29px;background:var(--red);border-radius:15px;font-size:11px;font-weight:700;display:flex;align-items:center;justify-content:center}
.search{top:94px;left:936px;width:173px;border-bottom:1px solid #888;font-size:12px;font-weight:600;padding-bottom:6px}
.search svg{position:absolute;right:0;top:0}

/* hero */
.hero{top:130px;height:539px;background:linear-gradient(120deg,#3d4644,#5c6664 45%,#2f3635);color:var(--white);text-align:center}
.hero-headline{top:98px;left:0;width:1200px;font-size:33px;line-height:38px;letter-spacing:2px}
.hero-sub{top:278px;left:0;width:1200px;font-size:21px;line-height:26px}
.btn{display:flex;align-items:center;justify-content:center;border-radius:20px;font-size:14px;font-weight:500}
.btn-light{top:389px;left:410px;width:188px;height:34px;background:var(--white);color:var(--red)}
.btn-red{top:389px;left:612px;width:178px;height:34px;background:var(--red);color:var(--white)}
.play-video{top:456px;left:510px;width:180px;height:42px;background:#3b3b3b;font-size:15px;font-weight:700;display:flex;align-items:center;justify-content:center;gap:12px}

/* quote */
.quote{top:669px;height:276px}
.quote-box{top:54px;left:326px;width:549px;height:167px;border:5px solid #c9c9c9;display:flex;align-items:center;justify-content:center;text-align:center}
.quote-box p{font-size:20px;line-height:26px;letter-spacing:1.5px;color:#333;padding:0 20px;margin-top:14px}
.target-badge{background:var(--white);padding:0 14px}
.quote .target-badge{top:36px;left:580px}

/* instructor */
.instructor{top:945px;height:736px;background:var(--light)}
.portrait{top:145px;left:89px;width:476px;height:476px;border-radius:50%;border:3px solid var(--red);background:radial-gradient(circle at 50% 40%,#d8d8d8,#8a8a8a 60%,#3c3c3c)}
.instr-icon{top:98px;left:606px}
.instr-kicker{top:101px;left:680px;font-size:15px;color:#333}
.instr-name{top:122px;left:680px;font-size:21px;color:var(--red);letter-spacing:1px}
.instr-name b{color:#333;font-weight:400}
.instr-copy{top:172px;left:607px;width:500px;font-size:13.4px;line-height:21px;color:#444}
.instr-copy p+p{margin-top:21px}

/* as seen on */
.press{top:1681px;height:181px}
.press-title{top:36px;left:0;width:1200px;text-align:center;font-size:14px;color:#333;letter-spacing:1px}
.press-title i{display:inline-block;width:8px;height:8px;border-radius:50%;background:var(--red);margin:0 5px;vertical-align:1px;opacity:.8}
.press-row{top:86px;left:350px;width:500px;display:flex;justify-content:space-between;align-items:center}
.press-row span{font-size:20px;font-weight:700;color:#1e1e1e}

/* levels */
.levels{top:1862px;height:787px;background:var(--dark);color:var(--white)}
.levels-icon{top:92px;left:90px}
.levels-title{top:88px;left:178px;font-size:33px;line-height:38px;letter-spacing:1px}
.levels-copy{top:237px;left:176px;width:574px;font-size:13.4px;line-height:21px}
.levels-copy p+p{margin-top:21px}
.learn-more{top:394px;left:869px;width:148px;height:34px;background:var(--red);border-radius:18px;font-size:14px;font-weight:500;display:flex;align-items:center;justify-content:center}
.level{display:flex;align-items:center;gap:10px;font-size:14px;font-weight:500;line-height:21px}
.level .num{font-family:"Audiowide",sans-serif;font-size:50px;color:var(--gray-num);line-height:1}

/* video */
.video{top:2649px;height:677px;background:#000}
.globe{top:60px;left:380px;width:440px;height:460px;border-radius:50%;background:radial-gradient(circle at 55% 45%,#4a5a3a,#1d2a33 55%,#05080a 75%)}
.video-title{top:304px;left:0;width:1200px;text-align:center;font-size:42px;letter-spacing:7px;color:var(--gold)}
.progress{top:570px;left:36px;width:1128px;height:4px;background:#555}
.progress i{display:block;width:72px;height:4px;background:#ddd}
.controls{top:610px;left:36px;width:1128px;display:flex;align-items:center;gap:22px;color:#eee;font-size:20px}

/* success */
.success{top:3326px;height:514px}
.success .target-badge{top:80px;left:575px}
.success-title{top:148px;left:0;width:1200px;text-align:center;font-size:29px;color:#333;letter-spacing:1px}
.story{top:236px;width:270px}
.story q{display:block;font-style:italic;font-size:13.4px;line-height:21px;color:#555;quotes:"\201C" "\201D"}
.story hr{border:0;border-top:2px solid var(--red);width:30px;margin:20px 0 12px;opacity:.7}
.story h4{font-family:"Audiowide",sans-serif;font-weight:400;font-size:15px;color:#333;letter-spacing:1px}
.story small{font-size:12px;color:#666}

/* contact */
.contact{top:3840px;height:639px;background:var(--dark)}
.trainer-card{top:115px;left:169px;width:366px;height:376px;background:var(--white);border:2px solid #ccc;padding:42px 40px 0 40px}
.trainer-card h3{font-family:"Audiowide",sans-serif;font-weight:400;font-size:18px;color:var(--red);letter-spacing:1px}
.trainer-card h2{font-family:"Audiowide",sans-serif;font-weight:400;font-size:20px;color:#333;letter-spacing:1px;margin-top:4px}
.trainer-card .creds{font-size:11.5px;line-height:20px;color:#444;margin-top:14px}
.info{display:flex;gap:12px;font-size:13px;line-height:20px;color:#777;margin-top:12px}
.info svg{flex:none;margin-top:3px}
.info b{color:#555;font-weight:600}
.field{left:583px;width:447px;background:var(--white);border:2px solid #ccc;font-size:13px;font-weight:600;color:#999;padding:17px 38px}
.field sup{color:var(--red)}
.submit{top:530px;left:841px;width:189px;height:56px;background:var(--red);color:var(--white);font-size:16px;font-weight:700;display:flex;align-items:center;justify-content:center}

.site-footer{top:4479px;height:52px;background:var(--darker);border-top:1px solid #555;color:#eee;font-size:12px;text-align:center;line-height:52px}
</style>
</head>
<body>

<header class="site-header">
  <nav class="utility-links abs"><span>Home</span><span>Upcoming Classes</span><span>Shop</span><span>Videos</span></nav>
  <div class="brand abs"><i></i>Brisklane Wardens</div>
  <div class="tagline abs display">PREPARED TO PREVAIL</div>
  <nav class="main-nav abs"><span>Falcon Institute</span><span>Testimonials</span><span>About</span><span>Lost Certificate</span></nav>
  <div class="login abs">&#9711; Log In</div>
  <div class="urgent abs">I NEED IMMEDIATE SERVICE</div>
  <div class="search abs">Search
    <svg width="14" height="14" viewBox="0 0 14 14"><circle cx="6" cy="6" r="4.5" fill="none" stroke="#ccc" stroke-width="1.5"/><line x1="9.5" y1="9.5" x2="13" y2="13" stroke="#ccc" stroke-width="1.5"/></svg>
  </div>
</header>

<section class="hero" role="img" aria-label="Civilian students practising at an outdoor shooting range">
  <h1 class="hero-headline abs display">DON’T BE FOOLED.<br>ALL CONCEALED WEAPONS<br>CLASSES ARE NOT CREATED<br>EQUAL</h1>
  <p class="hero-sub abs">There is a difference<br>Hands on training<br>Real world scenarios</p>
  <div class="btn btn-light abs">FALCON INSTITUTE</div>
  <div class="btn btn-red abs">GET TICKETS NOW</div>
  <div class="play-video abs">Play Video
    <svg width="26" height="20" viewBox="0 0 26 20"><rect x="1" y="1" width="24" height="18" fill="none" stroke="#fff" stroke-width="2"/><polygon points="10,5 18,10 10,15" fill="#fff"/></svg>
  </div>
</section>

<section class="quote">
  <div class="quote-box abs"><p class="display">"YOUR LIFE MAY DEPEND ON WHAT YOU LEARN IN YOUR CONCEALED CARRY TRAINING - DON'T SETTLE FOR A GUN SHOP CLASS!"</p></div>
  <div class="target-badge abs">
    <svg width="40" height="40" viewBox="0 0 40 40"><circle cx="20" cy="20" r="17" fill="none" stroke="#e21f26" stroke-width="3"/><circle cx="20" cy="20" r="10" fill="none" stroke="#e21f26" stroke-width="3"/><circle cx="20" cy="20" r="4" fill="#e21f26"/><path d="M20 0v6M20 34v6M0 20h6M34 20h6" stroke="#e21f26" stroke-width="2"/></svg>
  </div>
</section>

<section class="instructor">
  <div class="portrait abs" role="img" aria-label="Portrait of instructor Morgan Pellbrook"></div>
  <svg class="instr-icon abs" width="52" height="52" viewBox="0 0 40 40"><circle cx="20" cy="20" r="17" fill="none" stroke="#e21f26" stroke-width="3"/><circle cx="20" cy="20" r="10" fill="none" stroke="#e21f26" stroke-width="3"/><circle cx="20" cy="20" r="4" fill="#e21f26"/><path d="M20 0v6M20 34v6M0 20h6M34 20h6" stroke="#e21f26" stroke-width="2"/></svg>
  <div class="instr-kicker abs">ABOUT THE INSTRUCTOR</div>
  <div class="instr-name abs display">MORGAN <b>PELLBROOK</b></div>
  <div class="instr-copy abs">
    <p>Morgan Pellbrook is a 3rd generation Harborview native and delighted to be a part of this great community. He is a true security expert with 25 years of experience in the security industry. He has appeared on Vantage News, Keystone TV, Orbit One &amp; Meridian Seven news outlets. He has been Featured in numerous publications and has trained thousands to protect themselves and their homes from thugs and thieves. He is certified by both the NFTA &amp; the NWDLA as a firearms instructor. He is also an NFTA Range Safety Officer and Defensive Pistol Instructor. He often says: "My students are like family so I take their security personal. I want them to feel confident that they can protect themselves and their families!"</p>
    <p>Brisklane Wardens is a radically different concealed carry class focusing on the TRUTH about how "Real Attacks" take place. The Concealed Carry Class goes over way more than just the boring, lecture-style, gun shop curriculum into real strategies, tactics and training suggestions to help you prepare! You have to experience it to believe it! We also offer The Falcon Institute for those who are looking for a Fully Immersive, Reality Based training environment that prepares you to defend against the worst threats you may face! In The Institute, we utilize high tech, military/law enforcement grade simulators to take training to a level never before seen in the world of concealed carry.</p>
  </div>
</section>

<section class="press">
  <div class="press-title abs display"><i></i><i></i><i></i> AS SEEN ON <i></i><i></i><i></i></div>
  <div class="press-row abs"><span>Vantage News</span><span>Meridian Seven</span><span>Keystone TV</span><span>Orbit One</span></div>
</section>

<section class="levels">
  <svg class="levels-icon abs" width="52" height="52" viewBox="0 0 40 40"><circle cx="20" cy="20" r="17" fill="none" stroke="#e21f26" stroke-width="3"/><circle cx="20" cy="20" r="10" fill="none" stroke="#e21f26" stroke-width="3"/><circle cx="20" cy="20" r="4" fill="#e21f26"/><path d="M20 0v6M20 34v6M0 20h6M34 20h6" stroke="#e21f26" stroke-width="2"/></svg>
  <h2 class="levels-title abs display">OUR 7 LEVELS OF<br>TRAINING TAKE YOU<br>FROM ZERO TO HERO</h2>
  <div class="levels-copy abs">
    <p>Wanna hear something funny? Guess what the average person asks about a concealed weapons class? "How much is it and how long is it?" Can you believe it? We are talking about preparing you for life and death situations and the main concern is "How Fast" and "How Cheap?" WOW!</p>
    <p>Why do most people settle for a cheap &amp; quick concealed carry class? It's a fair question! Could you imagine a military soldier trained by a 2-hour class? How effective would they be in the heat of battle? If you want to be ready to SURVIVE an attack, YOU NEED MORE than a basic, run of the mill class! That's why we created a PROPRIETARY 7 LEVEL TRAINING SYSTEM to take you all the way to the peak of readiness!</p>
  </div>
  <div class="learn-more abs">Learn more</div>
  <div class="level abs" style="top:550px;left:176px"><span class="num">1</span>CONCEALED<br>CARRY CLASS</div>
  <div class="level abs" style="top:550px;left:384px"><span class="num">2</span>DYNAMIC DEFENSIVE<br>SHOOTING</div>
  <div class="level abs" style="top:550px;left:660px"><span class="num">3</span>FINE TUNING YOUR<br>TECHNIQUE</div>
  <div class="level abs" style="top:550px;left:938px"><span class="num">4</span>VIRTUAL<br>THREAT-LAB</div>
  <div class="level abs" style="top:640px;left:176px"><span class="num">5</span>TACTICAL SKILLS<br>&amp; DRILLS</div>
  <div class="level abs" style="top:640px;left:384px"><span class="num">6</span>CLOSE QUARTERS<br>DEFENSE</div>
  <div class="level abs" style="top:640px;left:660px"><span class="num">7</span>LIVE SCENARIO<br>THREAT-LAB</div>
</section>

<section class="video">
  <div class="globe abs" role="img" aria-label="Video still of the Earth seen from space"></div>
  <div class="video-title abs display">A FALCON INSTITUTE PRODUCTION</div>
  <div class="progress abs"><i></i></div>
  <div class="controls abs">
    <svg width="20" height="24" viewBox="0 0 20 24"><polygon points="2,2 18,12 2,22" fill="#eee"/></svg>
    <svg width="32" height="24" viewBox="0 0 32 24"><polygon points="2,8 8,8 15,2 15,22 8,16 2,16" fill="#eee"/><path d="M20 7q4 5 0 10M24 4q7 8 0 16" fill="none" stroke="#eee" stroke-width="2"/></svg>
    <span>00:02 / 00:45</span>
    <svg style="margin-left:auto" width="24" height="24" viewBox="0 0 24 24" fill="none" stroke="#eee" stroke-width="3"><path d="M2 8V2h6M16 2h6v6M22 16v6h-6M8 22H2v-6"/></svg>
  </div>
</section>

<section class="success">
  <div class="target-badge abs">
    <svg width="50" height="50" viewBox="0 0 40 40"><circle cx="20" cy="20" r="17" fill="none" stroke="#e21f26" stroke-width="3"/><circle cx="20" cy="20" r="10" fill="none" stroke="#e21f26" stroke-width="3"/><circle cx="20" cy="20" r="4" fill="#e21f26"/><path d="M20 0v6M20 34v6M0 20h6M34 20h6" stroke="#e21f26" stroke-width="2"/></svg>
  </div>
  <h2 class="success-title abs display">SUCCESS STORIES</h2>
  <div class="story abs" style="left:146px;width:245px"><q>I had never held a gun when I took the Brisklane Wardens class and I'm hooked! I'm going all the way to level 7! Thank you Brisklane Wardens!</q><hr><h4>RENATA L.</h4><small>October 14, 2017</small></div>
  <div class="story abs" style="left:412px;width:275px"><q>I was mugged here in Harborview and lived in fear ever since. It stole my happiness and I became scared to go out. I'm a Level 4 student and I feel sorry for the next thug that tries me!</q><hr><h4>DELPHINE R.</h4><small>December 9, 2017</small></div>
  <div class="story abs" style="left:706px;width:350px"><q>I've been shooting for years and already had my concealed weapons license. My first class was a gun shop class and a waste of money. Morgan took the time to show me how to properly grip my gun and my shooting dramatically improved!</q><hr><h4>OWEN K.</h4><small>March 3 2018</small></div>
</section>

<section class="contact">
  <div class="trainer-card abs">
    <h3>MEET THE TRAINER:</h3>
    <h2>MORGAN PELLBROOK</h2>
    <p class="creds">NFTA FIREARMS INSTRUCTOR, NWDLA INSTRUCTOR &amp; TRAINING COUNSELLOR, NEWS CORRESPONDENT, AND SECURITY EXPERT</p>
    <div class="info"><svg width="12" height="16" viewBox="0 0 12 16"><path d="M6 0a6 6 0 0 1 6 6c0 4-6 10-6 10S0 10 0 6a6 6 0 0 1 6-6z" fill="#e21f26"/><circle cx="6" cy="6" r="2" fill="#fff"/></svg><span>P.O. Box 4410<br>Cedar Hollow, FL 32990</span></div>
    <div class="info"><svg width="14" height="14" viewBox="0 0 14 14"><path d="M3 0l3 3-2 2q2 3 5 5l2-2 3 3-2 3Q5 13 0 3z" fill="#e21f26"/></svg><b>LOCAL: 555-014-BRSK (2775)<br>TOLL-FREE: 855-0-WARDEN</b></div>
    <div class="info"><svg width="14" height="11" viewBox="0 0 14 11"><rect width="14" height="11" rx="1" fill="#e21f26"/><path d="M1 1l6 5 6-5" fill="none" stroke="#fff" stroke-width="1.3"/></svg><span>hello@brisklanewardens.example.com</span></div>
  </div>
  <div class="field abs" style="top:120px;height:55px">Name <sup>*</sup></div>
  <div class="field abs" style="top:197px;height:55px">Email <sup>*</sup></div>
  <div class="field abs" style="top:275px;height:55px">Phone</div>
  <div class="field abs" style="top:354px;height:136px">Message</div>
  <div class="submit abs">Submit</div>
</section>

<footer class="site-footer">Copyright Brisklane Wardens 2021 - All Rights Reserved</footer>

</body>
</html>
```